Präsentationsvorlagen für eine internistisch-allgemeinmedizinische Arztpraxis
Zielgruppe
Wir sind eine internistisch-allgemeinmedizinische Arztpraxis
Die Folien werden sowohl für Fachvortröge aber auch für Patientenvorträge genutzt
Aufgabenstellung
Hätte gerne einen Vorschlag für 2 Versionen Format 16:9 und 4:3
Des Weiteren hätte ich gerne einen Bereich in der Präsentation wo man Studien/Literaturzutate ersichtlich darstellen kann.

```html
<!DOCTYPE html>
<html lang="de">
<head>
<meta charset="utf-8">
<title>Praxis am Lindenhain – Präsentationsvorlage</title>
<link href="https://fonts.googleapis.com/css2?family=Montserrat:wght@300;400;500;700;800;900&display=swap" rel="stylesheet">
<style>
  :root {
    --navy: #08145c;
    --blue: #0c4f8f;
    --teal: #1a8fb0;
    --cyan: #12c8d6;
    --grey: #6f7c8a;
    --text: #3c4a5a;
    --white: #ffffff;
  }
  * { margin: 0; padding: 0; box-sizing: border-box; }
  html, body { width: 1200px; height: 2981px; overflow: hidden; }
  body {
    font-family: "Montserrat", sans-serif;
    background: linear-gradient(180deg, #00b9ec 0%, #0a78b0 30%, #0b6ba3 55%, #0a86b6 80%, #00ccd8 100%);
    position: relative;
  }
  .slide {
    position: absolute; left: 57px; width: 1085px; height: 687px;
    background: var(--white); overflow: hidden;
    box-shadow: 14px 14px 22px rgba(0, 30, 70, .35);
  }
  .slide > svg.deco { position: absolute; left: 0; top: 0; }
  .slide-cover { top: 47px; }
  .slide-services { top: 778px; }
  .slide-steps { top: 1511px; }
  .slide-organs { top: 2241px; }

  .brand { position: absolute; font-weight: 800; color: var(--navy); white-space: nowrap; letter-spacing: -.2px; }
  .brand-large { left: 611px; top: 70px; font-size: 32px; }
  .brand-small { left: 0; right: 0; text-align: center; top: 633px; font-size: 18px; }

  .cover-title { position: absolute; left: 644px; top: 245px; font-size: 55px; line-height: 64px; font-weight: 900; color: var(--navy); }
  .cover-text { position: absolute; left: 621px; top: 513px; width: 340px; font-size: 13.5px; line-height: 22px; color: var(--teal); }

  .section-title { position: absolute; left: 0; right: 0; top: 75px; text-align: center; font-size: 53px; font-weight: 900; color: var(--navy); }
  .section-lead { position: absolute; left: 230px; width: 625px; top: 163px; text-align: center; font-size: 19.5px; line-height: 26px; color: var(--teal); }
  .service { position: absolute; top: 300px; width: 180px; margin-left: -90px; text-align: center; }
  .service svg { display: block; margin: 0 auto; }
  .service h3 { margin-top: 14px; font-size: 19.5px; font-weight: 500; color: var(--teal); letter-spacing: .5px; }
  .service p { margin-top: 16px; font-size: 12px; line-height: 19.5px; color: var(--text); padding: 0 20px; }

  .step-badge { position: absolute; border-radius: 50%; background: var(--cyan); color: var(--white); display: flex; align-items: center; justify-content: center; font-weight: 300; }
  .step-badge.big { width: 92px; height: 92px; font-size: 48px; }
  .step-title { position: absolute; font-size: 30px; font-weight: 900; color: var(--navy); }
  .step-sub { position: absolute; font-size: 19px; color: var(--teal); letter-spacing: .5px; }
  .step-text { position: absolute; font-size: 12px; line-height: 19.5px; color: var(--text); text-align: center; }

  .organ-label { position: absolute; font-size: 17px; line-height: 20px; color: var(--grey); letter-spacing: 1px; font-weight: 400; }
  .organ-label b { font-weight: 700; }
  .organ-label.left { text-align: right; width: 120px; }
  .step-badge.small { width: 46px; height: 46px; font-size: 24px; font-weight: 700; }
</style>
</head>
<body>

<!-- Cover -->
<section class="slide slide-cover">
  <svg class="deco" width="1085" height="687" viewBox="0 0 1085 687">
    <defs>
      <linearGradient id="coverRing" x1="0" y1="0" x2="0" y2="1">
        <stop offset="0" stop-color="#11c3d2"/>
        <stop offset=".5" stop-color="#0b5d9c"/>
        <stop offset="1" stop-color="#07125a"/>
      </linearGradient>
      <linearGradient id="coverPhoto" x1="0" y1="0" x2="1" y2="1">
        <stop offset="0" stop-color="#7fa6c4"/>
        <stop offset=".5" stop-color="#c9d4dc"/>
        <stop offset="1" stop-color="#5b7186"/>
      </linearGradient>
      <linearGradient id="dotBlue" x1="0" y1="0" x2="1" y2="1">
        <stop offset="0" stop-color="#0d6aa8"/>
        <stop offset="1" stop-color="#08145c"/>
      </linearGradient>
      <linearGradient id="arcLine" x1="0" y1="0" x2="0" y2="1">
        <stop offset="0" stop-color="#08145c"/>
        <stop offset="1" stop-color="#15b3c8"/>
      </linearGradient>
    </defs>
    <circle cx="95" cy="343" r="444" fill="url(#coverRing)"/>
    <circle cx="60" cy="343" r="372" fill="url(#coverPhoto)" role="img" aria-label="Foto: Arzt kniet lachend neben einer älteren Patientin im Rollstuhl"/>
    <circle cx="85" cy="343" r="520" fill="none" stroke="url(#arcLine)" stroke-width="2.5"/>
    <circle cx="546" cy="103" r="37" fill="url(#dotBlue)"/>
    <circle cx="601" cy="280" r="16" fill="url(#dotBlue)"/>
    <circle cx="571" cy="528" r="14" fill="url(#dotBlue)"/>
  </svg>
  <div class="brand brand-large">Praxis am Lindenhain</div>
  <h1 class="cover-title">Headline<br>Presentation</h1>
  <p class="cover-text">Lorem ipsum dolor sit amet, consectetuer adipiscing elit, sed diam nonummy nibh euismod tincidunt</p>
</section>

<!-- Services overview -->
<section class="slide slide-services">
  <svg width="0" height="0" style="position:absolute">
    <defs>
      <linearGradient id="iconDisc" x1="0" y1="0" x2="0" y2="1">
        <stop offset="0" stop-color="#0d7fb5"/>
        <stop offset="1" stop-color="#08145c"/>
      </linearGradient>
    </defs>
  </svg>
  <h2 class="section-title">Lorem ipsum</h2>
  <p class="section-lead">Lorem ipsum dolor sit amet, consectetuer adipiscing elit, sed diam nonummy nibh euismod tincidunt ut laoreet dolore magna aliquam erat volutpat. Ut wisi enim ad minim veniam,</p>

  <div class="service" style="left:204px">
    <svg width="106" height="106" viewBox="0 0 106 106">
      <circle cx="53" cy="53" r="53" fill="url(#iconDisc)"/>
      <path d="M22 42h42l16 14v18H22z" fill="#fff"/>
      <circle cx="34" cy="75" r="7" fill="#08145c" stroke="#fff" stroke-width="3"/>
      <circle cx="70" cy="75" r="7" fill="#08145c" stroke="#fff" stroke-width="3"/>
      <circle cx="48" cy="56" r="9" fill="#08145c"/>
      <path d="M46 50h4v4h4v4h-4v4h-4v-4h-4v-4h4z" fill="#fff"/>
    </svg>
    <h3>TITLE 01</h3>
    <p>Dolor sit amet, consectetuer adipiscing elit, sed diam nonummy nibh euismod tincidunt ut laoreet dolore magna aliquam erat volutpat.</p>
  </div>

  <div class="service" style="left:430px">
    <svg width="106" height="106" viewBox="0 0 106 106">
      <circle cx="53" cy="53" r="53" fill="url(#iconDisc)"/>
      <path d="M33 38h40c0 12-9 18-20 18s-20-6-20-18z" fill="#fff"/>
      <rect x="50" y="55" width="6" height="26" fill="#fff"/>
      <rect x="40" y="80" width="26" height="5" rx="2" fill="#fff"/>
    </svg>
    <h3>TITLE 02</h3>
    <p>Dolor sit amet, consectetuer adipiscing elit, sed diam nonummy nibh euismod tincidunt ut laoreet dolore magna aliquam erat volutpat.</p>
  </div>

  <div class="service" style="left:657px">
    <svg width="106" height="106" viewBox="0 0 106 106">
      <circle cx="53" cy="53" r="53" fill="url(#iconDisc)"/>
      <path d="M53 84C30 66 22 56 22 43c0-10 8-17 17-17 6 0 11 3 14 8 3-5 8-8 14-8 9 0 17 7 17 17 0 13-8 23-31 41z" fill="#fff"/>
      <path d="M28 55h16l5-10 6 20 5-10h18" fill="none" stroke="#08145c" stroke-width="3" stroke-linejoin="round"/>
    </svg>
    <h3>TITTLE 03</h3>
    <p>Dolor sit amet, consectetuer adipiscing elit, sed diam nonummy nibh euismod tincidunt ut laoreet dolore magna aliquam erat volutpat.</p>
  </div>

  <div class="service" style="left:884px">
    <svg width="106" height="106" viewBox="0 0 106 106">
      <circle cx="53" cy="53" r="53" fill="url(#iconDisc)"/>
      <path d="M37 20h32v14H37z" fill="#fff"/>
      <path d="M51 23h4v3h3v4h-3v3h-4v-3h-3v-4h3z" fill="#08145c"/>
      <path d="M34 40h38v34c0 7-8 12-19 12s-19-5-19-12z" fill="#fff"/>
      <path d="M40 46h26v24c0 4-6 7-13 7s-13-3-13-7z" fill="#08145c"/>
    </svg>
    <h3>TITLE 04</h3>
    <p>Dolor sit amet, consectetuer adipiscing elit, sed diam nonummy nibh euismod tincidunt ut laoreet dolore magna aliquam erat volutpat.</p>
  </div>

  <div class="brand brand-small">Praxis am Lindenhain</div>
</section>

<!-- Two steps -->
<section class="slide slide-steps">
  <svg class="deco" width="1085" height="687" viewBox="0 0 1085 687">
    <defs>
      <linearGradient id="stepRingA" x1="1" y1="0" x2="0" y2="1">
        <stop offset="0" stop-color="#0d6aa8"/>
        <stop offset="1" stop-color="#08145c"/>
      </linearGradient>
      <linearGradient id="stepRingB" x1="0" y1="0" x2="1" y2="1">
        <stop offset="0" stop-color="#0a5f9c"/>
        <stop offset=".6" stop-color="#12c3d2"/>
      </linearGradient>
      <linearGradient id="photoDevice" x1="0" y1="0" x2="1" y2="1">
        <stop offset="0" stop-color="#e6ecf0"/>
        <stop offset=".6" stop-color="#b9c4cc"/>
        <stop offset="1" stop-color="#8fa0ae"/>
      </linearGradient>
      <linearGradient id="photoScan" x1="0" y1="0" x2="1" y2="1">
        <stop offset="0" stop-color="#8d99ab"/>
        <stop offset=".5" stop-color="#d7a58c"/>
        <stop offset="1" stop-color="#b87a60"/>
      </linearGradient>
      <linearGradient id="dotStep" x1="0" y1="0" x2="1" y2="1">
        <stop offset="0" stop-color="#0d6aa8"/>
        <stop offset="1" stop-color="#08145c"/>
      </linearGradient>
    </defs>
    <circle cx="161" cy="167" r="206" fill="url(#stepRingA)"/>
    <circle cx="161" cy="167" r="188" fill="#fff"/>
    <circle cx="161" cy="167" r="184" fill="#8d9bc3"/>
    <circle cx="161" cy="167" r="176" fill="url(#photoDevice)" role="img" aria-label="Foto: Ultraschallgerät im Behandlungsraum"/>
    <path d="M20 345 Q 300 250 488 344 Q 585 392 636 450 Q 690 515 740 590" fill="none" stroke="#08145c" stroke-width="2.5"/>
    <circle cx="488" cy="344" r="37" fill="url(#dotStep)"/>
    <circle cx="636" cy="450" r="16" fill="url(#dotStep)"/>
    <circle cx="907" cy="535" r="235" fill="url(#stepRingB)"/>
    <circle cx="907" cy="535" r="213" fill="#fff"/>
    <circle cx="907" cy="535" r="207" fill="#9fdbe3"/>
    <circle cx="907" cy="535" r="195" fill="url(#photoScan)" role="img" aria-label="Foto: Hand führt einen Ultraschallkopf über den Bauch"/>
  </svg>

  <div class="step-badge big" style="left:472px;top:66px">01</div>
  <div class="step-title" style="left:594px;top:76px">Lorem Ipsum Dolor</div>
  <div class="step-sub" style="left:594px;top:120px">SUBTITLE 01</div>
  <p class="step-text" style="left:476px;top:180px;width:405px">Lorem ipsum dolor sit amet, consectetuer adipiscing elit, sed diam nonummy nibh euismod tincidunt ut laoreet dolore magna aliquam erat volutpat. Ut wisi enim ad minim veniam, quis nostrud exerci tation ullamcorper suscipit lobortis nisl ut aliquip ex ea commodo consequat. Duis autem vel eum iriure dolor in hendrerit in vulputate velit esse</p>

  <div class="step-badge big" style="left:124px;top:427px">02</div>
  <div class="step-title" style="left:245px;top:437px">Lorem Ipsum Dolor</div>
  <div class="step-sub" style="left:245px;top:481px">SUBTITLE 02</div>
  <p class="step-text" style="left:118px;top:542px;width:478px">Lorem ipsum dolor sit amet, consectetuer adipiscing elit, sed diam nonummy nibh euismod tincidunt ut laoreet dolore magna aliquam erat volutpat. Ut wisi enim ad minim veniam, quis nostrud exerci tation ullamcorper suscipit lobortis nisl ut aliquip ex ea commodo consequat. Duis autem vel eum iriure dolor in hendrerit in vulputate</p>

  <div class="brand brand-small" style="top:636px">Praxis am Lindenhain</div>
</section>

<!-- Organ overview -->
<section class="slide slide-organs">
  <svg class="deco" width="1085" height="687" viewBox="0 0 1085 687">
    <defs>
      <linearGradient id="ringOuter" x1="0" y1="0" x2="1" y2="1">
        <stop offset="0" stop-color="#08145c"/>
        <stop offset=".45" stop-color="#0c5a98"/>
        <stop offset=".7" stop-color="#12c3d2"/>
        <stop offset="1" stop-color="#0a6aa6"/>
      </linearGradient>
      <linearGradient id="ringInner" x1="1" y1="0" x2="0" y2="1">
        <stop offset="0" stop-color="#0d6aa8"/>
        <stop offset=".6" stop-color="#12c3d2"/>
        <stop offset="1" stop-color="#08145c"/>
      </linearGradient>
      <linearGradient id="organGlow" x1="0" y1="0" x2="0" y2="1">
        <stop offset="0" stop-color="#2fd2dc"/>
        <stop offset="1" stop-color="#137a9a"/>
      </linearGradient>
    </defs>
    <circle cx="541" cy="336" r="236" fill="none" stroke="url(#ringOuter)" stroke-width="28"/>
    <path d="M541 100 A236 236 0 0 1 760 250" fill="none" stroke="#12c3d2" stroke-width="28" stroke-opacity=".55"/>
    <circle cx="541" cy="336" r="172" fill="none" stroke="url(#ringInner)" stroke-width="32"/>
    <circle cx="541" cy="336" r="156" fill="#08145c"/>
    <ellipse cx="541" cy="336" rx="62" ry="130" fill="url(#organGlow)" opacity=".85" role="img" aria-label="Illustration: menschliche Organe – Lunge, Herz, Leber und Darm"/>
  </svg>

  <div class="organ-label left" style="left:148px;top:131px"><b>LOREM</b><br>IPSUM<br>DOLOR</div>
  <div class="step-badge small" style="left:285px;top:119px">01</div>
  <div class="step-badge small" style="left:743px;top:122px">03</div>
  <div class="organ-label" style="left:806px;top:131px"><b>LOREM</b><br>IPSUM<br>DOLOR</div>

  <div class="organ-label left" style="left:148px;top:513px"><b>LOREM</b><br>IPSUM<br>DOLOR</div>
  <div class="step-badge small" style="left:285px;top:501px">02</div>
  <div class="step-badge small" style="left:743px;top:503px">04</div>
  <div class="organ-label" style="left:806px;top:513px"><b>LOREM</b><br>IPSUM<br>DOLOR</div>

  <div class="brand brand-small" style="top:638px">Praxis am Lindenhain</div>
</section>

</body>
</html>
```